Hot air balloon tour company needs a brochure redesign

Look for a fresh new brochure design. Using company logo and colours.
Modern, simple and professional look required
Font styles to use
Sans Serif
Colors
0054AA
0677BA
7BADD7
CADEEF
E8F1F8

```html
<!DOCTYPE html>
<html lang="en">
<head>
<meta charset="utf-8">
<title>Skyreach Ballooning Brochure</title>
<link rel="stylesheet" href="https://fonts.googleapis.com/css2?family=Oswald:wght@300;400;500&family=PT+Sans+Narrow:wght@400;700&display=swap">
<style>
  :root {
    --navy: #0054AA;
    --blue: #0677BA;
    --sky: #7BADD7;
    --mist: #CADEEF;
    --ice: #E8F1F8;
    --night: #231b18;
    --ink: #1b1b1b;
    --white: #ffffff;
    --backdrop: #dcdcdc;
  }
  * { box-sizing: border-box; margin: 0; padding: 0; }
  html, body { width: 1200px; height: 1091px; overflow: hidden; }
  body { background: var(--backdrop); position: relative; font-family: "PT Sans Narrow", sans-serif; }

  .spread { position: absolute; left: 270px; width: 660px; height: 506px; display: flex; box-shadow: 0 6px 14px rgba(0,0,0,.25); }
  .spread--outside { top: 24px; }
  .spread--inside { top: 561px; }
  .panel { position: relative; width: 220px; height: 100%; overflow: hidden; }
  .panel--sky { background: var(--sky); }
  .panel--night { background: var(--night); }

  .cloud { position: absolute; height: 7px; border-radius: 4px; background: var(--ice); }
  .cloud::before { content: ""; position: absolute; left: 25%; top: -5px; width: 50%; height: 8px; border-radius: 5px; background: var(--ice); }

  /* outside – features panel */
  .feature { position: absolute; left: 0; width: 100%; }
  .feature__ribbon { position: relative; height: 26px; width: 196px; background: var(--ink); clip-path: polygon(0 0, 100% 0, 92% 100%, 0 100%); }
  .feature__dot { position: absolute; left: 10px; top: 2px; width: 18px; height: 22px; border-radius: 50% 50% 45% 45%; background: var(--mist); border: 2px solid #d8d9a6; }
  .feature__title { position: absolute; left: 36px; top: 4px; font-family: "Oswald", sans-serif; font-weight: 400; font-size: 12px; line-height: 18px; white-space: nowrap; color: var(--white); }
  .feature__body { padding: 6px 18px 0 18px; font-size: 11px; line-height: 1.5; color: var(--ink); }
  .offer__title { position: absolute; top: 316px; width: 100%; text-align: center; font-family: "Oswald", sans-serif; font-weight: 400; font-size: 24px; color: var(--white); }
  .offer__body { position: absolute; top: 360px; left: 14px; right: 14px; text-align: center; font-size: 15px; line-height: 1.6; color: var(--ink); }
  .offer__body em { font-style: normal; color: var(--white); }

  /* outside – cover back panel */
  .night-cut { position: absolute; inset: 0; }
  .balloon-art { position: absolute; left: 68px; top: 55px; width: 86px; height: 118px; border-radius: 50% 50% 45% 45% / 55% 55% 45% 45%; background: linear-gradient(180deg, var(--blue) 0%, #5a6470 45%, #2a2a2e 100%); }
  .brand { position: absolute; width: 100%; text-align: center; font-family: "Oswald", sans-serif; font-weight: 500; letter-spacing: 1px; color: var(--blue); }
  .brand__sub { display: block; font-size: 11px; font-weight: 400; letter-spacing: 2px; color: var(--white); }
  .contact { position: absolute; width: 100%; text-align: center; color: var(--white); }
  .contact__phone { font-family: "Oswald", sans-serif; font-weight: 300; font-size: 19px; }
  .contact__line { font-size: 12px; margin-top: 4px; }
  .social { position: absolute; top: 460px; width: 100%; display: flex; justify-content: center; gap: 10px; }
  .social__square { width: 17px; height: 17px; border-radius: 3px; background: var(--navy); }
  .social__square--warm { background: #d6417b; }

  /* cover photo panel */
  .photo { position: absolute; }
  .photo--cover { inset: 0; background: linear-gradient(180deg, #8f9592 0%, #9fa39b 45%, #7f7552 68%, #6b5a34 85%, #8a6a3a 100%); }
  .tagline { position: absolute; top: 282px; width: 100%; text-align: center; font-family: "Oswald", sans-serif; font-weight: 400; font-size: 34px; color: var(--white); }

  /* inside */
  .headline { position: absolute; top: 20px; width: 100%; text-align: center; font-family: "Oswald", sans-serif; font-weight: 400; font-size: 28px; line-height: 1.5; color: var(--sky); }
  .photo--basket { left: 0; top: 217px; width: 100%; height: 165px; background: linear-gradient(180deg, #f1f1f1 0%, #bdbdbd 55%, #6f6f6f 100%); }
  .heading { position: absolute; width: 100%; text-align: center; font-family: "Oswald", sans-serif; font-weight: 400; color: var(--white); text-transform: uppercase; }
  .heading--crew { top: 22px; font-size: 22px; line-height: 1.3; z-index: 2; }
  .photo--sunrise { left: 0; top: 78px; width: 100%; bottom: 0; background: linear-gradient(180deg, #c9b79a 0%, #e8b25a 22%, #a98550 40%, #5b4a35 65%, #3a2f26 100%); }
  .heading--flex { top: 22px; font-size: 22px; }
  .heading--flex span { color: var(--navy); }
  .photo--oval { left: 16px; top: 88px; width: 190px; height: 280px; border-radius: 50%; background: linear-gradient(180deg, #6e8fb8 0%, #a7b5c4 40%, #8c7d55 70%, #9b7a3e 100%); }
  .heading--award { top: 390px; font-size: 26px; line-height: 1.2; }
  .heading--award b { font-weight: 500; }
</style>
</head>
<body>

<section class="spread spread--outside">
  <div class="panel panel--sky features">
    <div class="feature" style="top:30px">
      <div class="feature__ribbon"><span class="feature__dot"></span><span class="feature__title">Experienced Pilots &amp; Crew</span></div>
      <p class="feature__body">Lorem ipsum dolor sit amet, consectetuer adipiscing elit, sed diam nonummy nibh euismod tincidunt ut laoreet dolore</p>
    </div>
    <div class="feature" style="top:128px">
      <div class="feature__ribbon"><span class="feature__dot"></span><span class="feature__title">Award winning service</span></div>
      <p class="feature__body">Lorem ipsum dolor sit amet, consectetuer adipiscing elit, sed diam nonummy nibh euismod tincidunt ut laoreet dolore</p>
    </div>
    <div class="feature" style="top:226px">
      <div class="feature__ribbon"><span class="feature__dot"></span><span class="feature__title">Daily Flights</span></div>
      <p class="feature__body">Lorem ipsum dolor sit amet, consectetuer adipiscing elit, sed diam nonummy nibh euismod tincidunt ut laoreet dolore</p>
    </div>
    <h2 class="offer__title">We offer</h2>
    <p class="offer__body"><em>Lorem Ipsum</em> Dolor Sit Amet Consectetuer <em>Adipiscing</em> <em>Elit Sed Diam</em> Nonummy Nibh Euismod Tincidunt Ut <em>Laoreet Dolore</em></p>
    <span class="cloud" style="left:160px; top:486px; width:34px"></span>
  </div>

  <div class="panel panel--sky back">
    <svg class="night-cut" width="220" height="506" viewBox="0 0 220 506" aria-hidden="true">
      <polygon points="0,74 220,94 220,506 0,506" fill="var(--night)"/>
    </svg>
    <span class="cloud" style="left:18px; top:40px; width:40px"></span>
    <span class="cloud" style="left:158px; top:26px; width:36px"></span>
    <div class="balloon-art" role="img" aria-label="Illustration of a blue and grey hot air balloon"></div>
    <div class="brand" style="top:235px; font-size:24px">Skyreach<span class="brand__sub">Ballooning</span></div>
    <div class="contact" style="top:375px">
      <div class="contact__phone">1300 555 019</div>
      <div class="contact__line">info@skyreachballooning.com.au</div>
      <div class="contact__line">www.skyreachballooning.com.au</div>
    </div>
    <div class="social"><span class="social__square"></span><span class="social__square social__square--warm"></span></div>
  </div>

  <div class="panel cover">
    <div class="photo photo--cover" role="img" aria-label="Photo of a brown and green checked hot air balloon over hills and vineyard posts"></div>
    <p class="tagline">get on!!</p>
    <div class="brand" style="top:350px; font-size:22px">Skyreach<span class="brand__sub">Ballooning</span></div>
  </div>
</section>

<section class="spread spread--inside">
  <div class="panel panel--night intro">
    <h1 class="headline">The beautiful<br>Hunter Valley<br>in a<br>Hot Air Ballon</h1>
    <div class="photo photo--basket" role="img" aria-label="Black and white photo of a balloon basket full of passengers"></div>
    <div class="brand" style="top:405px; font-size:24px">Skyreach<span class="brand__sub">Ballooning</span></div>
    <div class="contact" style="top:457px">
      <div class="contact__line">(1300 555 019)</div>
      <div class="contact__line" style="margin-top:2px">www.skyreachballooning.com.au</div>
    </div>
  </div>

  <div class="panel panel--sky crew">
    <h2 class="heading heading--crew">Experienced<br>Pilots &amp;<br>Crew</h2>
    <div class="photo photo--sunrise" role="img" aria-label="Photo of passengers watching a balloon rise at sunrise over misty valley"></div>
    <span class="cloud" style="left:170px; top:88px; width:30px; z-index:2"></span>
  </div>

  <div class="panel panel--sky service">
    <h2 class="heading heading--flex">Flight <span>Flexibility</span></h2>
    <span class="cloud" style="left:170px; top:72px; width:32px"></span>
    <div class="photo photo--oval" role="img" aria-label="Oval photo of a checked hot air balloon above a misty grassy field"></div>
    <span class="cloud" style="left:20px; top:366px; width:36px"></span>
    <h2 class="heading heading--award">Award<br><b>Winning</b><br>Service</h2>
  </div>
</section>

</body>
</html>
```